Improved Business Card, Government Contracting

We are looking to update the design of our business cards. We would like to create a template that can be used for future employees and easy to update.

Halvorsen Advisory Partners, LLC is a Service Disabled Veteran Owned Small Business with headquarters located in Ashcombe, NR. Our current website is www.hapteam.com. We have contracts in KS and VA with expansion opportunities in various other states. Our primary line of work is within government contracting and providing consulting services to various organizations within the Bureau of Frontier Works. We would like to project a professional image of our company that is consistent with the industry. Provided are previous versions of our business card template that shows our logo as well. We would like to make sure the information on the cards are easily noticeable .

Target Market(s)

Government Officials
Fellow Small Business Contractors
Large Business Contractors (ex. TRUX, Keswell Barnaby, Pryde Okonjo Whitcombe)

Industry/Entity Type

Business

Contact Information for Business Card

Dale Fenwick
Office Manager
Halvorsen Advisory Partners
Ph: 555.555.0172
Email: d.fenwick@hapteam.us
www.hapteam.com

Requirements
Must have
• The business mailing address is:
• 31842 204th Lane
• Ashcombe, NR 66099
Nice to have
• Embossed lettering

```html
<!DOCTYPE html>
<html lang="en">
<head>
<meta charset="utf-8">
<title>Halvorsen Advisory Partners – Business Card</title>
<link rel="stylesheet" href="https://fonts.googleapis.com/css2?family=Roboto:ital,wght@0,400;0,700;1,400&display=swap">
<style>
  :root {
    --navy: #2a2d8c;
    --yellow: #f2e600;
    --paper: #f7f7f5;
    --backdrop: #d9d9d7;
    --white: #ffffff;
  }
  * { margin: 0; padding: 0; box-sizing: border-box; }
  html, body {
    width: 1200px; height: 1200px; overflow: hidden;
    background: var(--backdrop);
    font-family: "Roboto", Arial, sans-serif;
  }
  .sheet {
    width: 1200px; height: 1200px;
    display: flex; flex-direction: column;
    align-items: center; justify-content: center; gap: 64px;
  }
  .card {
    position: relative; width: 800px; height: 457px;
    background: var(--paper); overflow: hidden;
    box-shadow: 0 6px 18px rgba(0,0,0,.18);
  }
  .card-shapes { position: absolute; inset: 0; }

  /* contact side */
  .contact { position: absolute; left: 44px; top: 46px; color: var(--yellow); }
  .contact-name { font-size: 34px; font-weight: 400; color: var(--white); letter-spacing: .5px; }
  .contact-name .first { font-weight: 700; color: var(--yellow); }
  .contact-role { font-size: 19px; font-style: italic; margin-top: 2px; }
  .contact-company { font-size: 19px; font-weight: 700; color: var(--white); margin-top: 2px; }
  .contact-list { list-style: none; margin-top: 22px; }
  .contact-list li { display: flex; align-items: flex-start; gap: 16px; font-size: 19px; line-height: 1.3; margin-bottom: 8px; }
  .contact-list svg { flex: none; width: 18px; height: 18px; margin-top: 3px; }

  .side-name {
    position: absolute; left: 520px; top: 186px; width: 230px;
    text-align: center; color: var(--navy);
    font-size: 26px; font-weight: 700; line-height: 1.2;
  }

  /* front side */
  .front-name {
    position: absolute; left: 90px; top: 110px; width: 400px;
    display: flex; align-items: center; gap: 18px;
    color: var(--navy); font-size: 38px; font-weight: 700; line-height: 1.1;
  }
  .front-name .mark { flex: none; width: 26px; height: 26px; background: var(--yellow); }
  .front-web {
    position: absolute; left: 168px; top: 272px;
    color: var(--navy); font-size: 25px; letter-spacing: .5px;
  }
</style>
</head>
<body>
<main class="sheet">

  <section class="card card-contact">
    <svg class="card-shapes" viewBox="0 0 800 457" aria-hidden="true">
      <rect x="0" y="0" width="480" height="457" fill="var(--navy)"/>
      <polygon points="0,0 78,0 0,40" fill="var(--yellow)"/>
      <polygon points="400,457 480,457 480,408" fill="var(--yellow)"/>
      <rect x="770" y="0" width="30" height="400" fill="var(--yellow)"/>
      <polygon points="800,380 800,457 758,457" fill="var(--navy)"/>
    </svg>
    <div class="contact">
      <h1 class="contact-name"><span class="first">DALE</span> FENWICK</h1>
      <p class="contact-role">(Office Manager)</p>
      <p class="contact-company">Halvorsen Advisory Partners</p>
      <ul class="contact-list">
        <li>
          <svg viewBox="0 0 18 18"><path d="M9 1a6 6 0 0 0-6 6c0 4.5 6 10 6 10s6-5.5 6-10a6 6 0 0 0-6-6z" fill="var(--yellow)"/><circle cx="9" cy="7" r="2.3" fill="var(--navy)"/></svg>
          <span>31842 204th Lane,<br>Ashcombe, NR 66099</span>
        </li>
        <li>
          <svg viewBox="0 0 18 18"><rect x="4" y="1" width="10" height="16" rx="2" fill="var(--yellow)"/><rect x="6" y="3" width="6" height="10" fill="var(--navy)"/></svg>
          <span>555.555.0172</span>
        </li>
        <li>
          <svg viewBox="0 0 18 18"><rect x="1" y="3" width="16" height="12" rx="1" fill="var(--yellow)"/><path d="M2 4l7 6 7-6" fill="none" stroke="var(--navy)" stroke-width="1.5"/></svg>
          <span>d.fenwick@hapteam.us</span>
        </li>
        <li>
          <svg viewBox="0 0 18 18"><circle cx="9" cy="9" r="8" fill="var(--yellow)"/><circle cx="9" cy="9" r="3.5" fill="none" stroke="var(--navy)" stroke-width="1.6"/></svg>
          <span>www.hapteam.com</span>
        </li>
      </ul>
    </div>
    <p class="side-name">Halvorsen<br>Advisory<br>Partners</p>
  </section>

  <section class="card card-front">
    <svg class="card-shapes" viewBox="0 0 800 457" aria-hidden="true">
      <polygon points="0,0 60,0 0,32" fill="var(--navy)"/>
      <polygon points="800,62 800,405 752,457 330,457" fill="var(--navy)"/>
    </svg>
    <h2 class="front-name"><span class="mark"></span><span>Halvorsen Advisory Partners</span></h2>
    <p class="front-web">www.hapteam.com</p>
  </section>

</main>
</body>
</html>
```